Website for enterprise software start-up

We need a new Wordpress website. We are an early stage start-up focused on mobile video technology for cellular operators. The audience is strategy, marketing and customer acquisition execs from the operators.

The purpose of the site is to act as a sales brochure and capture leads. A demo app can be downloaded from the current site, want to put that behind a contact form.

Current website is at www.brevlane.tv. Similar number of pages. Looking for a clean design template, with minimal customization. Blog will remain as is.

Want to be able to modify the copy via Wordpress. Reference designs I like: tarnwick.com, tessel4analytics.com

Target Market(s)

Mobile operators and MVNOs in the US and Asia Pacific regions

Industry/Entity Type

Business Software

Coding

Coded - Design and coding required

Number of Pages Required

4 page

Font styles to use
Sans Serif

Colors
f78f20

Requirements
Must have
• Form for downloading sample apps.
• Landing page with image, Product, Blog, About, Contact
• Team page

```html
<!DOCTYPE html>
<html lang="en">
<head>
<meta charset="utf-8">
<title>Brevlane – Smarter Mobile Video Moments</title>
<link rel="stylesheet" href="https://fonts.googleapis.com/css2?family=Montserrat:wght@300;400;500;600;700&display=swap">
<style>
  :root {
    --brand-orange: #f78f20;
    --ink: #3a3a3a;
    --ink-soft: #4a4a4a;
    --muted: #9a9a9a;
    --white: #ffffff;
    --section-bg: #f6f7f9;
    --hairline: #e3e4e6;
  }
  * { box-sizing: border-box; margin: 0; padding: 0; }
  html, body { width: 1200px; height: 930px; overflow: hidden; }
  body {
    font-family: "Montserrat", Arial, sans-serif;
    color: var(--ink);
    background: var(--section-bg);
    position: relative;
  }

  /* Header */
  .site-header {
    position: absolute; left: 0; top: 0; width: 1200px; height: 60px;
    background: var(--white);
    box-shadow: 0 1px 2px rgba(0,0,0,.12);
    z-index: 2;
  }
  .brand {
    position: absolute; left: 234px; top: 15px;
    display: flex; align-items: center; gap: 6px;
    text-decoration: none;
  }
  .brand-mark { width: 30px; height: 30px; background: var(--brand-orange); }
  .brand-name {
    font-size: 27px; font-weight: 600; color: var(--ink);
    letter-spacing: -0.5px; line-height: 30px;
  }
  .main-nav {
    position: absolute; left: 674px; top: 19px;
    display: flex; align-items: center; height: 23px;
  }
  .main-nav a {
    font-size: 10px; font-weight: 600; letter-spacing: .8px;
    color: var(--ink); text-decoration: none; margin-right: 22px;
  }
  .main-nav a.nav-login {
    margin: 0 0 0 -10px; background: var(--brand-orange); color: var(--white);
    height: 23px; line-height: 23px; padding: 0 10px; border-radius: 3px;
  }

  /* Hero */
  .hero {
    position: absolute; left: 0; top: 60px; width: 1200px; height: 553px;
    overflow: hidden;
  }
  .hero-photo {
    position: absolute; inset: 0;
    background:
      linear-gradient(90deg, rgba(60,55,50,.25) 0%, rgba(60,55,50,0) 60%),
      linear-gradient(90deg, #8c8782 0%, #958c84 35%, #8e7563 60%, #6b4c36 78%, #4a3528 100%);
  }
  .hero-content { position: absolute; left: 234px; top: 198px; color: var(--white); }
  .hero-title { font-size: 26px; font-weight: 500; letter-spacing: .2px; }
  .hero-lead { margin-top: 17px; font-size: 14.5px; font-weight: 400; line-height: 21px; width: 420px; }
  .hero-actions { margin-top: 40px; display: flex; gap: 9px; }
  .btn {
    display: flex; align-items: center; justify-content: center; gap: 6px;
    width: 156px; height: 31px; border-radius: 16px;
    font-size: 11.5px; font-weight: 600; letter-spacing: .3px;
    color: var(--white); text-decoration: none;
  }
  .btn-primary { background: var(--brand-orange); }
  .btn-outline { border: 1.5px solid var(--white); }

  /* Features */
  .features { position: absolute; left: 0; top: 613px; width: 1200px; height: 317px; }
  .features-title {
    position: absolute; top: 67px; width: 100%; text-align: center;
    font-size: 26px; font-weight: 400; color: var(--ink-soft);
  }
  .features-intro {
    position: absolute; top: 109px; width: 100%; text-align: center;
    font-size: 12px; line-height: 14px; color: var(--muted);
  }
  .device {
    position: absolute; left: 499px; top: 193px; width: 207px; height: 140px;
    border-radius: 30px 30px 0 0;
    background: linear-gradient(180deg, #f5efe6 0%, #e7dccb 60%, #9a8566 100%);
  }
  .feature { position: absolute; top: 230px; width: 260px; }
  .feature-left { left: 157px; text-align: right; }
  .feature-right { left: 735px; }
  .feature-icon {
    position: absolute; top: 0; width: 42px; height: 42px; border-radius: 50%;
    background: var(--white); border: 1px solid var(--hairline);
    display: flex; align-items: center; justify-content: center;
  }
  .feature-left .feature-icon { left: 271px; }
  .feature-right .feature-icon { left: 0; }
  .feature-body { position: absolute; top: 13px; width: 200px; }
  .feature-left .feature-body { right: 0; }
  .feature-right .feature-body { left: 50px; }
  .feature-name { font-size: 12px; font-weight: 500; color: var(--ink-soft); }
  .feature-text { margin-top: 4px; font-size: 10.5px; line-height: 12.7px; color: var(--muted); }
</style>
</head>
<body>
  <header class="site-header">
    <a class="brand" href="#"><span class="brand-mark"></span><span class="brand-name">brevlane</span></a>
    <nav class="main-nav">
      <a href="#">PRODUCT</a>
      <a href="#">CONTACT</a>
      <a href="#">BLOG</a>
      <a href="#">ABOUT</a>
      <a href="#" class="nav-login">LOGIN</a>
    </nav>
  </header>

  <section class="hero">
    <div class="hero-photo" role="img" aria-label="Young woman in a knit beanie and sunglasses smiling at her smartphone on a city street"></div>
    <div class="hero-content">
      <h1 class="hero-title">Smarter Mobile Video Moments</h1>
      <p class="hero-lead">We engage mobile audiences with the right video content at the perfect moment.</p>
      <div class="hero-actions">
        <a class="btn btn-primary" href="#">DOWNLOD APP</a>
        <a class="btn btn-outline" href="#">
          <svg width="16" height="16" viewBox="0 0 16 16"><circle cx="8" cy="8" r="7" fill="none" stroke="#fff" stroke-width="1.3"/><path d="M6.3 5 L11 8 L6.3 11 Z" fill="#fff"/></svg>
          WATCH VIDEO
        </a>
      </div>
    </div>
  </section>

  <section class="features">
    <h2 class="features-title">Our Features</h2>
    <p class="features-intro">Personalised flawless HD videos, revealed at the perfect<br>moment, as rich media notifications.</p>

    <div class="device" role="img" aria-label="Smartphone showing a video notification"></div>

    <div class="feature feature-left">
      <div class="feature-body">
        <h3 class="feature-name">Nice Graphix</h3>
        <p class="feature-text">Reach your mobile audience<br>with beautiful HD thumbnails<br>and in-notification videos.</p>
      </div>
      <div class="feature-icon">
        <svg width="18" height="18" viewBox="0 0 18 18"><path d="M16 2 L8 10 L9.5 11.5 Z" fill="#555"/><path d="M7 10.5 C4.5 10.5 4.5 13 3 15 C6 15 9 14 9 12 Z" fill="#555"/></svg>
      </div>
    </div>

    <div class="feature feature-right">
      <div class="feature-icon">
        <svg width="18" height="18" viewBox="0 0 18 18"><path d="M16 2 C11 2 8 5 6 9 L9 12 C13 10 16 7 16 2 Z" fill="#555"/><path d="M6 9 L2.5 9 L5 6.5 L8 6.5 Z M9 12 L9 15.5 L11.5 13 L11.5 10 Z" fill="#555"/><path d="M5 12 L2 16 L6 13 Z" fill="#555"/></svg>
      </div>
      <div class="feature-body">
        <h3 class="feature-name">High Speed Delivery</h3>
        <p class="feature-text">Instant video playback, zero<br>buffering, guaranteed flawless<br>playback - even when offline.</p>
      </div>
    </div>
  </section>
</body>
</html>
```